Structural Engineering Business Card

Veltrow Drafts does residential house plans for clients in Central Florida. Would like simple but elegant business card that is appropriate for a house plan engineering company. Prefer black business card with black/white them but open to other shades of blue. I uploaded a sample card that I came across that looked good but please come up with your own creative designs.

Contact Information for Business Card

Name, Title, Phone, Email, Address, website

```html
<!DOCTYPE html>
<html lang="en">
<head>
<meta charset="utf-8">
<title>Veltrow Drafts – Business Card</title>
<link href="https://fonts.googleapis.com/css2?family=Arimo:wght@400;700&display=swap" rel="stylesheet">
<style>
  :root {
    --page-bg: #e9e9ea;
    --card-dark: #353535;
    --card-back: #2c2c2c;
    --ink-white: #ffffff;
    --ink-soft: #d6d6d6;
    --rule: #a9a9a9;
    --pattern-a: #262626;
    --pattern-b: #3c3c3c;
  }
  * { box-sizing: border-box; margin: 0; padding: 0; }
  html, body {
    width: 1200px; height: 802px; overflow: hidden;
    background: var(--page-bg);
    font-family: "Arimo", Arial, sans-serif;
  }
  .stage {
    position: relative; width: 1200px; height: 802px;
    display: flex; align-items: center; justify-content: center; gap: 20px;
  }
  .card {
    position: relative; width: 540px; height: 310px; overflow: hidden;
    box-shadow: 0 6px 18px rgba(0,0,0,.22);
  }
  /* front */
  .card-front { background: var(--card-dark); color: var(--ink-white); }
  .brand {
    position: absolute; display: flex; align-items: center; gap: 10px;
    font-weight: 700; color: var(--ink-white); letter-spacing: .5px;
  }
  .brand-mark { width: 16px; height: 16px; background: var(--ink-white); }
  .card-front .brand { left: 170px; top: 56px; font-size: 30px; }
  .divider {
    position: absolute; left: 30px; right: 30px; top: 128px;
    height: 1px; background: var(--rule);
  }
  .address {
    position: absolute; right: 30px; top: 146px; text-align: right;
    font-size: 15px; line-height: 1.35; color: var(--ink-soft);
  }
  .person { position: absolute; left: 30px; top: 178px; }
  .person-name { font-weight: 700; font-size: 18px; letter-spacing: .5px; }
  .person-title { font-size: 14px; color: var(--ink-soft); }
  .person-rule { width: 210px; height: 1px; background: var(--rule); margin: 7px 0 7px; }
  .contacts { list-style: none; font-size: 14px; line-height: 1.5; color: var(--ink-white); }
  .contacts li { display: flex; align-items: center; gap: 8px; }
  .contacts svg { width: 12px; height: 12px; flex: none; }
  .edge-stripe-thin {
    position: absolute; left: 0; right: 0; bottom: 13px; height: 3px; background: var(--ink-white);
  }
  .edge-stripe-wide {
    position: absolute; left: 0; right: 0; bottom: 0; height: 8px; background: var(--ink-white);
  }
  /* back */
  .card-back { background: var(--card-back); }
  .back-pattern {
    position: absolute; inset: 0;
    background: linear-gradient(135deg, var(--pattern-a) 0%, var(--pattern-b) 55%, var(--pattern-a) 100%);
  }
  .card-back .brand {
    left: 50%; top: 50%; transform: translate(-50%, -50%); font-size: 32px; white-space: nowrap;
  }
</style>
</head>
<body>
<main class="stage">
  <section class="card card-front" aria-label="Business card front">
    <div class="brand"><span class="brand-mark"></span>VELTROW DRAFTS</div>
    <div class="divider"></div>
    <p class="address">Your Address, City<br>State, Zip 0000</p>
    <div class="person">
      <p class="person-name">MARCUS ELLERY</p>
      <p class="person-title">Manager</p>
      <div class="person-rule"></div>
      <ul class="contacts">
        <li>
          <svg viewBox="0 0 12 12"><circle cx="6" cy="6" r="6" fill="#fff"/><path d="M4 3.2l1 1.3-.6.7a4 4 0 0 0 2.4 2.4l.7-.6 1.3 1-.6 1A5 5 0 0 1 3 4z" fill="#353535"/></svg>
          321-555-0148
        </li>
        <li>
          <svg viewBox="0 0 12 12"><rect x="0.5" y="2" width="11" height="8" fill="#fff"/><path d="M1 2.5l5 4 5-4" stroke="#353535" fill="none"/></svg>
          hello@veltrowdrafts.com
        </li>
        <li>
          <svg viewBox="0 0 12 12"><circle cx="6" cy="6" r="6" fill="#fff"/><circle cx="6" cy="6" r="4" fill="none" stroke="#353535"/><path d="M2 6h8M6 2v8" stroke="#353535"/></svg>
          www.veltrowdrafts.com
        </li>
      </ul>
    </div>
    <div class="edge-stripe-thin"></div>
    <div class="edge-stripe-wide"></div>
  </section>

  <section class="card card-back" aria-label="Business card back">
    <div class="back-pattern" role="img" aria-label="Repeating embossed tonal pattern across the card back"></div>
    <div class="brand"><span class="brand-mark"></span>VELTROW DRAFTS</div>
  </section>
</main>
</body>
</html>
```